Clear tides coaching programme

I need a flyer designed to promote my coaching programme. The programme is designed to help people who are feeling a bit lost in their life, looking for new possiblities or that they want more focus in their goals. It is an intensive programme designed to help people achieve real change in their lives. It is a premium product targeted at senior managers, directors and business leaders. I care passionately about helping people achieve their potential. I would like the design to fit with the logo (attached) and I've drafted the content (also attached). I would like it to be A5 and affordable to print - so not full colour.

```html
<!DOCTYPE html>
<html lang="en">
<head>
<meta charset="utf-8">
<title>Clear tides coaching programme</title>
<link rel="stylesheet" href="https://fonts.googleapis.com/css2?family=Bree+Serif&family=Open+Sans:ital,wght@0,700;0,800;1,600;1,700&display=swap">
<style>
  :root {
    --ink: #111111;
    --accent-red: #e3101a;
    --page-light: #ffffff;
    --page-grey: #d6d6d6;
    --quote-band: #c9c9c9;
    --footer-bar: #0c0c0c;
    --footer-text: #ffffff;
    --hero-light: #e4e4e4;
    --hero-mid: #a8a8a8;
    --hero-dark: #4a4a4a;
  }
  html, body {
    margin: 0;
    padding: 0;
    overflow: hidden;
    background: #ffffff;
  }
  .flyer {
    position: relative;
    width: 846px;
    height: 1200px;
    overflow: hidden;
    background: linear-gradient(90deg, var(--page-light) 0%, #f0f0f0 45%, var(--page-grey) 100%);
    color: var(--ink);
    font-family: "Open Sans", Arial, sans-serif;
    font-weight: 800;
  }
  .hero {
    position: absolute;
    left: 0; top: 0;
    width: 846px; height: 362px;
    background: linear-gradient(120deg, var(--hero-dark) 0%, var(--hero-mid) 35%, var(--hero-light) 65%, var(--hero-mid) 100%);
  }
  .hero-title {
    position: absolute;
    left: 380px; top: 60px;
    margin: 0;
    font-family: "Bree Serif", Georgia, serif;
    font-weight: 400;
    font-size: 52px;
    line-height: 52px;
    color: var(--ink);
    -webkit-text-stroke: 0.8px var(--ink);
    white-space: nowrap;
  }
  .section-heading {
    position: absolute;
    left: 42px;
    margin: 0;
    font-size: 25px;
    font-weight: 800;
    line-height: 30px;
    letter-spacing: 0.6px;
    white-space: nowrap;
  }
  .heading-are-you { top: 370px; }
  .heading-why { top: 901px; }
  .question-list {
    position: absolute;
    left: 42px; top: 408px;
    margin: 0; padding: 0;
    list-style: none;
    font-size: 23px;
    line-height: 28px;
    letter-spacing: 0.6px;
    white-space: nowrap;
  }
  .call-to-move {
    position: absolute;
    left: 42px; top: 533px;
    margin: 0;
    font-size: 26px;
    line-height: 32px;
    letter-spacing: 0.6px;
    color: var(--accent-red);
    white-space: nowrap;
  }
  .call-to-move .full-stop { color: var(--ink); }
  .quote-band {
    position: absolute;
    left: 0; top: 578px;
    width: 846px; height: 67px;
    margin: 0;
    padding: 0;
    background: linear-gradient(90deg, #dcdcdc 0%, var(--quote-band) 100%);
  }
  .quote-text {
    margin: 0;
    padding-top: 4px;
    text-align: center;
    font-style: italic;
    font-weight: 700;
    font-size: 25px;
    line-height: 29px;
    letter-spacing: 0.2px;
    white-space: nowrap;
  }
  .quote-author { font-style: normal; font-weight: 800; }
  .body-copy {
    position: absolute;
    left: 42px;
    margin: 0;
    font-size: 22px;
    font-weight: 800;
    line-height: 24.6px;
    letter-spacing: 0.8px;
    white-space: nowrap;
  }
  .programme-copy { top: 652px; }
  .about-copy { top: 943px; }
  .contact-bar {
    position: absolute;
    left: 0; top: 1132px;
    width: 846px; height: 68px;
    background: var(--footer-bar);
    color: var(--footer-text);
    text-align: center;
    font-size: 30px;
    font-weight: 700;
    line-height: 60px;
    letter-spacing: 0.8px;
  }
</style>
</head>
<body>
<main class="flyer">
  <div class="hero" role="img" aria-label="Black and white photograph of one climber on a rock summit reaching down to help another climber up, against a bright sky"></div>

  <h1 class="hero-title">Push Yourself to<br>reach your dreams</h1>

  <h2 class="section-heading heading-are-you">Are you:</h2>
  <ul class="question-list">
    <li>Fed up but unsure how to move on?</li>
    <li>Finding it hard to focus?</li>
    <li>Dreaming of what could come next in your life?</li>
    <li>Looking for new opportunities ad possibilities?</li>
  </ul>
  <p class="call-to-move">Then its time to move on<span class="full-stop">.</span></p>

  <blockquote class="quote-band">
    <p class="quote-text">“The secret of change is to focus all your energy not on<br>fighting the old, but on building the new.” <span class="quote-author">~ Elian Varro</span></p>
  </blockquote>

  <p class="body-copy programme-copy">So make the first step towards a happier life and take up your<br>own personality tailored “Clear tides” coaching journey.<br>This program consist&nbsp; of 6 face to face coaching sessions, each<br>90 minutes long and carefully designed around you, your needs<br>and goals.&nbsp; You will also benefit from free email support in<br>between your sessions, development feedback, recommended<br>resources to support your journey and bespoke action plan.<br>The programme will help you achieve your goals and increase<br>your satisfaction with your work and home life.</p>

  <h2 class="section-heading heading-why">Why work with me?</h2>
  <p class="body-copy about-copy">I’m a coach and transformational leader with a decade of<br>experience in delivering better results for individuals,<br>organisations and customers.&nbsp; I’m passionate about helping<br>people achieve their potential and find new possibilities.<br>So take the first step towards your own “Clear tides” and<br>book a free 15 minute phone or Vidora consultation by emailing<br>me at:</p>

  <footer class="contact-bar">reachingyourpotential@tidemail.net</footer>
</main>
</body>
</html>
```